Counseling Practice Business Card

I need a professional looking business card incorporating my new logo that was just completed. Card needs to incorporate my name and title, description of my specialty, my address, my phone number, my fax number, my email and my website URL. I need to be able to choose design on/with different paper colors and textures.
I do not have a lot of business card ideas so I am open to anything but I want bold,sharp, clear card without additional designs other than my logo (see attached file info). I am open to different color backgrounds or paper colors including black. I do not like traditional brackets around area codes in phone number or dashes between numbers in phone number. Am open to other ways of presenting including periods between numbers as appropriate. I do not know enough to know what I like yet but I want card to coordinate and work together with my logo. My practice emphasizes natural mental health interventions so any use of color (with background paper color or the blue and green in my logo) that elicits nature is nice. In addition to black, any natural brown or wood looking background might be desirable also. Most of the offerings so far look very similar and boring.

Target Market(s)

Potential therapy clients and other professionals

Contact Information for Business Card

Card information:
Marcus T. Whitfield, Ph.D.
Licensed Clinical Psychologist
Integrative Health Coach
4812 Ferndale Pkwy NW
Suite 730
Duluth, GA 30096
(770) 555-0142 phone
(770) 555-0186 fax
drmarcuswhitfield@kelvora.com
pathbloomcounseling.com

Font styles to use
Serif
Sans Serif
Other font styles liked:
• anything that you think looks crisp, clear and easily readable

Requirements
Must have
• Any color used should coordinate with my logo design (see attached files).
• Card should be printed horizontally so top and bottom are longest sides of rectangle.
• Background color or paper color should complement and highlight logo. Do not like a white background. black, grey, brown or any color my logo would blend well with.
Nice to have
• I would like designer to utilize color to highlight letters/name or phone-fax-web symbols.
• Bottom edge of card could be highlighted if appropriate to an idea.
Should not have
• I would NOT want the card to have a pure white background at all.
• No clear cards.
• Cards should be oriented with long sides on bottom and top, NOT sides. DO NOT LIKE THIS THIN TALL ORIENTATION.

```html
<!DOCTYPE html>
<html lang="en">
<head>
<meta charset="utf-8">
<title>Pathbloom Counseling – Business Card</title>
<link href="https://fonts.googleapis.com/css2?family=Open+Sans:wght@400;600&display=swap" rel="stylesheet">
<style>
  :root {
    --page: #ffffff;
    --card-dark: #0f0f0f;
    --card-glow: #232323;
    --brand-green: #0b6b35;
    --brand-blue: #2a72bb;
    --text-light: #f2f2f2;
    --font-main: "Open Sans", Arial, sans-serif;
  }
  * { margin: 0; padding: 0; box-sizing: border-box; }
  html, body {
    width: 1200px; height: 720px; overflow: hidden;
    background: var(--page);
    font-family: var(--font-main);
  }
  .canvas { position: relative; width: 1200px; height: 720px; }

  .card {
    position: absolute;
    width: 444px; height: 274px;
    background: radial-gradient(ellipse at 50% 25%, var(--card-glow) 0%, var(--card-dark) 70%);
    box-shadow: 8px 10px 14px rgba(0,0,0,0.35);
    overflow: hidden;
  }
  .card--front { left: 106px; top: 208px; }
  .card--back  { left: 646px; top: 206px; }

  .edge-band {
    position: absolute; left: 0; bottom: 0;
    width: 100%; height: 10px; display: flex;
  }
  .edge-band__green { flex: 1; background: var(--brand-green); }
  .edge-band__blue  { flex: 1; background: var(--brand-blue); }

  .wordmark {
    position: absolute;
    color: var(--brand-blue);
    font-weight: 400;
    text-align: center;
    line-height: 1;
  }
  .wordmark__name { display: block; }
  .wordmark__sub { display: block; text-transform: uppercase; }

  .card--front .wordmark { left: 0; width: 100%; top: 98px; }
  .card--front .wordmark__name { font-size: 58px; letter-spacing: -0.5px; }
  .card--front .wordmark__sub { font-size: 17px; letter-spacing: 13px; margin-top: 6px; padding-left: 13px; }

  .card--back .wordmark { left: 26px; top: 40px; text-align: left; }
  .card--back .wordmark__name { font-size: 36px; letter-spacing: -0.3px; }
  .card--back .wordmark__sub { font-size: 11px; letter-spacing: 8.6px; margin-top: 3px; }

  .person { position: absolute; left: 26px; top: 116px; width: 392px; }
  .person__name { color: var(--brand-blue); font-size: 11.5px; line-height: 14px; }
  .person__title { color: var(--brand-green); font-size: 8px; line-height: 12px; }
  .person__rule { height: 2px; background: var(--brand-blue); margin-top: 2px; }

  .contact { position: absolute; left: 26px; color: var(--text-light); font-size: 8.6px; line-height: 12px; }
  .contact--address { top: 157px; }
  .contact--phones { top: 192px; font-weight: 600; }
  .contact--online { top: 222px; }
  .contact__row { display: flex; align-items: center; gap: 5px; }
  .contact__icon { width: 9px; height: 9px; flex: none; }
</style>
</head>
<body>
<main class="canvas">

  <section class="card card--front" aria-label="Card front">
    <div class="wordmark">
      <span class="wordmark__name">Pathbloom</span>
      <span class="wordmark__sub">Counseling</span>
    </div>
    <div class="edge-band"><span class="edge-band__green"></span><span class="edge-band__blue"></span></div>
  </section>

  <section class="card card--back" aria-label="Card back">
    <div class="wordmark">
      <span class="wordmark__name">Pathbloom</span>
      <span class="wordmark__sub">Counseling</span>
    </div>

    <div class="person">
      <p class="person__name">Marcus T. Whitfield, Ph.D.</p>
      <p class="person__title">Licensed Clinical Psychologist/ Integrative Health Coach</p>
      <div class="person__rule"></div>
    </div>

    <address class="contact contact--address" style="font-style:normal">
      <p>4812 Ferndale Pkwy NW Suite 730</p>
      <p>Duluth, GA 30096</p>
    </address>

    <div class="contact contact--phones">
      <p class="contact__row">
        <svg class="contact__icon" viewBox="0 0 10 10" aria-hidden="true"><path d="M2 0.8 L3.6 2.6 L2.8 3.6 Q4 6 6.4 7.2 L7.4 6.4 L9.2 8 L8 9.4 Q3.6 9 0.6 2 Z" fill="var(--brand-green)"/></svg>
        770 555 0142
      </p>
      <p class="contact__row">
        <svg class="contact__icon" viewBox="0 0 10 10" aria-hidden="true"><rect x="2.5" y="0.8" width="5" height="2.6" fill="var(--brand-green)"/><rect x="0.6" y="3.6" width="8.8" height="4" rx="0.8" fill="var(--brand-green)"/><rect x="2.5" y="6" width="5" height="3.2" fill="var(--brand-green)" stroke="var(--card-dark)" stroke-width="0.8"/></svg>
        770 555 0186
      </p>
    </div>

    <div class="contact contact--online">
      <p class="contact__row">
        <svg class="contact__icon" viewBox="0 0 10 10" aria-hidden="true"><circle cx="5" cy="5" r="4.3" fill="var(--brand-green)"/><path d="M0.7 5 H9.3 M5 0.7 V9.3 M5 0.7 Q2 5 5 9.3 M5 0.7 Q8 5 5 9.3" stroke="var(--card-dark)" stroke-width="0.6" fill="none"/></svg>
        drmarcuswhitfield@kelvora.com
      </p>
      <p class="contact__row">
        <svg class="contact__icon" viewBox="0 0 10 10" aria-hidden="true"><rect x="0.6" y="2" width="8.8" height="6" fill="none" stroke="var(--brand-green)" stroke-width="0.9"/><path d="M0.6 2 L5 5.6 L9.4 2" fill="none" stroke="var(--brand-green)" stroke-width="0.9"/></svg>
        pathbloomcounseling.com
      </p>
    </div>

    <div class="edge-band"><span class="edge-band__green"></span><span class="edge-band__blue"></span></div>
  </section>

</main>
</body>
</html>
```